Business Card Design Project

I need a business card for an environmentally friendly interior design company called Maplecrest Decor.
I was thinking it might be nice to print the business cards on brown recycled paper with green ink.
In addition to interior design, I will also be able to consult with homeowners regarding their indoor environments and how they might be affecting their health after May 2013 which is when I will complete my certification program. This can be added to the business card at that time: "Certified Dwelling Vitality Environmental Consultant".

```html
<!DOCTYPE html>
<html lang="en">
<head>
<meta charset="utf-8">
<title>Maplecrest Decor — Business Card</title>
<link href="https://fonts.googleapis.com/css2?family=Josefin+Sans:ital,wght@0,300;0,400;1,300&display=swap" rel="stylesheet">
<style>
  :root {
    --stage-light: #ffffff;
    --stage-peach: #e2b094;
    --paper: #9b6a48;
    --paper-dark: #86583a;
    --paper-light: #ad7c58;
    --ink-green: #1f9e45;
    --ink-cream: #f3e2d2;
    --ink-gold: #f1dca6;
  }
  * { margin: 0; padding: 0; box-sizing: border-box; }
  html, body { width: 1200px; height: 1000px; overflow: hidden; }
  body {
    position: relative;
    font-family: "Josefin Sans", sans-serif;
    background:
      linear-gradient(135deg, var(--stage-peach) 0%, #f3ddd0 22%, var(--stage-light) 45%, var(--stage-light) 55%, #f0d6c6 78%, var(--stage-peach) 100%);
  }
  .card {
    position: absolute;
    width: 813px;
    height: 465px;
    background:
      radial-gradient(ellipse 300px 160px at 20% 30%, var(--paper-light), transparent 70%),
      radial-gradient(ellipse 260px 180px at 75% 70%, var(--paper-dark), transparent 70%),
      radial-gradient(ellipse 340px 150px at 60% 20%, var(--paper-light), transparent 70%),
      radial-gradient(ellipse 280px 160px at 15% 85%, var(--paper-dark), transparent 70%),
      var(--paper);
    box-shadow: 0 0 2px rgba(0,0,0,0.15);
  }
  .card--front { left: 18px; top: 18px; }
  .card--back { left: 369px; top: 513px; height: 464px; }

  .brand {
    position: absolute;
    left: 205px;
    top: 150px;
    display: flex;
    align-items: center;
    gap: 22px;
    color: var(--ink-green);
  }
  .brand__mark {
    width: 70px; height: 70px;
    border-radius: 50%;
    background: var(--ink-green);
    flex: none;
  }
  .brand__name {
    font-weight: 400;
    font-size: 62px;
    line-height: 1.05;
    letter-spacing: 2px;
    text-transform: uppercase;
  }
  .tagline {
    position: absolute;
    left: 0; right: 0;
    top: 382px;
    text-align: center;
    padding-right: 0;
    transform: translateX(-2px);
    font-style: italic;
    font-weight: 300;
    font-size: 24px;
    letter-spacing: 2px;
    color: var(--ink-cream);
    width: 806px;
  }
  .tagline--front { left: -0px; width: 808px; }

  .contact {
    position: absolute;
    left: 0; width: 100%;
    top: 194px;
    text-align: center;
    color: var(--ink-gold);
  }
  .contact__name {
    font-weight: 300;
    font-size: 34px;
    letter-spacing: 3px;
    text-transform: uppercase;
  }
  .contact__phone {
    margin-top: 8px;
    font-weight: 300;
    font-size: 24px;
    letter-spacing: 2px;
  }
  .credential {
    position: absolute;
    left: 0; width: 100%;
    top: 416px;
    text-align: center;
    font-style: italic;
    font-weight: 300;
    font-size: 23px;
    letter-spacing: 1.5px;
    color: var(--ink-cream);
  }
</style>
</head>
<body>
  <section class="card card--front" aria-label="Card front">
    <div class="brand">
      <span class="brand__mark" aria-hidden="true"></span>
      <span class="brand__name">Maplecrest<br>Decor</span>
    </div>
    <p class="tagline tagline--front">Environmentally Friendly Design</p>
  </section>

  <section class="card card--back" aria-label="Card back">
    <div class="contact">
      <p class="contact__name">June Ann Marlow</p>
      <p class="contact__phone">555.204.7381</p>
    </div>
    <p class="credential">Certified Dwelling Vitality Environmental Consultant</p>
  </section>
</body>
</html>
```